Maple Hollow Skilled Nursing Facility

We are a skilled nursing facility that cares for elderly when they have come from the hospital and are trying to transition to make it back to their homes! We strive to create an environment that is friendly with great service to meet their needs and take care of them. The task is to create a website that informs the community of our excellent service and care. I will upload our logo and a brochure to give some ideas.
Target Market(s)
Families who will be looking at care facilities and rating them based on their quality for their loved ones.
Coding
Coded - Design and coding required
Number of Pages Required
5+ page
Requirements
Must have
- Social Media Integration.
Nice to have
- Nice, professional and clean. A warming website that is inviting to those who see.

```html
<!DOCTYPE html>
<html lang="en">
<head>
<meta charset="utf-8">
<title>Maple Hollow Post Acute</title>
<link rel="stylesheet" href="https://fonts.googleapis.com/css2?family=Cinzel:wght@400;700&family=Lato:ital,wght@0,400;0,700;1,400&family=Oswald:wght@400&display=swap">
<style>
:root{
  --blue:#0a63cc;
  --green:#7cc217;
  --ink:#111;
  --text:#333;
  --line:#d8d8d8;
  --footer:#262626;
  --footer-text:#e6e6e6;
}
*{margin:0;padding:0;box-sizing:border-box}
html,body{width:1200px;height:1064px;overflow:hidden}
body{position:relative;font-family:'Lato',sans-serif;color:var(--text);
  background:linear-gradient(#dcdcdc 595px,#fff 860px,#fff)}
.abs{position:absolute}
/* header */
.site-header{position:absolute;left:0;top:0;width:1200px;height:86px;background:#fafafa}
.brand{left:134px;top:17px;display:flex;align-items:center;gap:10px}
.brand-mark{width:54px;height:54px;border-radius:50%;background:var(--blue)}
.brand-name{font-family:'Cinzel',serif;font-size:22px;line-height:1.05;color:var(--ink)}
.brand-name small{display:block;font-size:13px;letter-spacing:1px;text-align:center}
.contact-top{right:137px;top:33px;display:flex;align-items:center;gap:14px;font-size:13px;color:#222}
.contact-top .phone{font-size:17px}
.contact-top span{display:flex;align-items:center;gap:6px}
/* nav */
.main-nav{position:absolute;left:0;top:86px;width:1200px;height:41px;background:var(--blue)}
.main-nav ul{list-style:none;display:flex;position:absolute;left:131px;top:0;height:41px}
.main-nav li{font-family:'Cinzel',serif;font-size:16px;letter-spacing:1px;color:#fff;
  height:41px;line-height:41px;text-align:center;border-left:1px solid rgba(255,255,255,.35)}
.main-nav li:first-child{border:0;background:#000}
/* hero */
.hero{position:absolute;left:0;top:127px;width:1200px;height:468px;
  background:
   linear-gradient(180deg,rgba(255,255,255,0) 60%,rgba(255,255,255,.15)),
   linear-gradient(90deg,#a67a5f 0%,#d6a286 14%,#e2b59c 24%,#8fb3dc 36%,#a8c6e6 44%,#dfe6ec 56%,#f1f4f6 70%,#f7f9fa 100%)}
.hero-title{position:absolute;right:133px;top:168px;text-align:right;font-family:'Oswald',sans-serif;
  font-weight:400;font-size:40px;line-height:46px;color:#000}
.dots{position:absolute;right:133px;top:330px;display:flex;gap:8px}
.dots i{width:14px;height:14px;border-radius:50%;background:#999}
.dots i:first-child{background:var(--blue)}
/* content card */
.content-card{position:absolute;left:131px;top:553px;width:938px;height:360px;background:#fff;
  box-shadow:0 0 12px rgba(0,0,0,.12)}
.col{position:absolute;top:16px}
.col h2{font-family:'Cinzel',serif;font-weight:400;font-size:23px;line-height:27px;color:var(--ink)}
.col h2 em{font-style:normal;color:var(--green)}
.rule{height:2px;background:var(--line);position:relative;margin-top:9px}
.rule::before{content:"";position:absolute;left:0;top:0;width:100px;height:2px;background:var(--blue)}
.divider{position:absolute;top:30px;width:1px;height:270px;background:#ececec}
.photo{margin-top:14px;width:263px;height:133px;background:linear-gradient(90deg,#cfdbe4,#f0f2f3 60%,#e8d6c6)}
.about-text{margin-top:10px;font-size:14px;line-height:21px;padding-left:2px}
.read-more{position:absolute;display:flex;height:24px;font-size:13px}
.read-more b{width:19px;background:#000;color:#fff;display:flex;align-items:center;justify-content:center;font-weight:400}
.read-more span{background:var(--green);color:#fff;padding:0 8px;line-height:24px;margin-left:2px}
.service{display:flex;gap:8px;padding:9px 0 8px;border-bottom:1px dotted #ccc}
.service.first{padding-top:14px}
.service.last{border:0}
.service-icon{width:40px;height:46px;background:#7d7d7d;border-radius:6px;flex:none;opacity:.8}
.service h3{font-size:20px;font-weight:700;color:var(--blue);line-height:22px}
.service p{font-size:13px;line-height:16px;color:#333;margin-top:3px}
.field{display:block;width:252px;height:32px;border:1px solid #bbb;margin-top:9px;
  padding:0 11px;font-size:13px;line-height:30px;color:#666}
.field.first{margin-top:14px}
.field.msg{height:75px}
.submit{margin-top:12px;width:94px;height:31px;background:var(--green);color:#fff;font-weight:700;
  font-size:16px;text-align:center;line-height:31px}
/* footer */
.site-footer{position:absolute;left:0;top:942px;width:1200px;height:122px;background:var(--footer);color:var(--footer-text);font-size:13.5px}
.foot-nav{left:134px;top:17px;display:flex;gap:12px}
.foot-nav span+span::before{content:"|";margin-right:12px}
.foot-item{display:flex;gap:10px;align-items:flex-start;line-height:19px}
.social{left:588px;top:49px;display:flex;gap:7px}
.social i{width:27px;height:27px;border:1.5px solid #ddd;border-radius:50%}
.subscribe{left:772px;top:22px;display:flex;width:297px;height:33px}
.subscribe .input{flex:1;background:#f4f4f4;color:#777;font-style:italic;font-size:12px;display:flex;align-items:center;gap:8px;padding-left:14px}
.subscribe .btn{width:92px;background:var(--blue);color:#fff;font-weight:700;font-size:13px;display:flex;align-items:center;justify-content:center}
.copyright{left:772px;top:74px;width:297px;text-align:center;line-height:17px}
</style>
</head>
<body>

<header class="site-header">
  <div class="abs brand">
    <div class="brand-mark"></div>
    <div class="brand-name">Maple Hollow<small>Post Acute</small></div>
  </div>
  <div class="abs contact-top">
    <span><svg width="18" height="12" viewBox="0 0 18 12"><rect width="18" height="12" fill="#0a63cc"/><path d="M0 0l9 7 9-7" fill="none" stroke="#fff" stroke-width="1.4"/></svg>info@maplehollowcare.com</span>
    <span class="phone"><svg width="15" height="16" viewBox="0 0 24 24"><path fill="#0a63cc" d="M6.6 10.8a15 15 0 006.6 6.6l2.2-2.2a1 1 0 011-.25 11.4 11.4 0 003.6.57 1 1 0 011 1V20a1 1 0 01-1 1A17 17 0 013 4a1 1 0 011-1h3.5a1 1 0 011 1c0 1.25.2 2.45.57 3.57a1 1 0 01-.25 1z"/></svg>(858) 555-0147</span>
  </div>
</header>

<nav class="main-nav">
  <ul>
    <li style="width:112px">Home</li>
    <li style="width:137px">About Us</li>
    <li style="width:150px">Services</li>
    <li style="width:169px">Resources</li>
    <li style="width:196px">Testimonials</li>
    <li style="width:180px">Contact Us</li>
  </ul>
</nav>

<section class="hero" role="img" aria-label="Photo of a smiling nurse with her arms around an elderly resident">
  <h1 class="hero-title">We Provide The Top Quality Nursing<br>Care &amp; Rehabilitaion Services To The<br>San Diego Community</h1>
  <div class="dots"><i></i><i></i><i></i></div>
</section>

<main class="content-card">
  <div class="col" style="left:16px;width:263px">
    <h2>About <em>Maple Hollow<br>Post Acute</em></h2>
    <div class="rule"></div>
    <div class="photo" role="img" aria-label="Photo of a smiling nurse with a clipboard and a doctor in the background"></div>
    <p class="about-text">Lorem ipsum dolor sit amet, consectetuer adipiscing elit, sed diam nonummy nibh euismod magna aliquam erat volutpat.</p>
  </div>
  <div class="read-more" style="left:18px;top:313px"><b>→</b><span>Read More</span></div>

  <div class="divider" style="left:308px"></div>

  <div class="col" style="left:338px;width:262px">
    <h2>Our<br><em>Services</em></h2>
    <div class="rule"></div>
    <div class="service first"><div class="service-icon" role="img" aria-label="Nursing care icon"></div><div><h3>Nursing Care</h3><p>Ut wisi enim ad minim venia m, quisip nostrud exerci tation ullamcor.</p></div></div>
    <div class="service"><div class="service-icon" role="img" aria-label="Rehabilitation icon"></div><div><h3>Rehabilitation</h3><p>Ut wisi enim ad minim venia m, quisip nostrud exerci tation ullamcor.</p></div></div>
    <div class="service last"><div class="service-icon" role="img" aria-label="Therapy services icon"></div><div><h3>Therapy Services</h3><p>Ut wisi enim ad minim venia m, quisip nostrud exerci tation ullamcor.</p></div></div>
  </div>
  <div class="read-more" style="left:339px;top:313px"><b>→</b><span>Read More</span></div>

  <div class="divider" style="left:629px"></div>

  <div class="col" style="left:660px;width:263px">
    <h2>Quick<br><em>Inquiry</em></h2>
    <div class="rule"></div>
    <div class="field first">Name</div>
    <div class="field">Email</div>
    <div class="field">Phone</div>
    <div class="field msg">Message</div>
    <div class="submit">SUBMIT</div>
  </div>
</main>

<footer class="site-footer">
  <div class="abs foot-nav"><span>Home</span><span>About Us</span><span>Services</span><span>Resources</span><span>Testimonials</span><span>Contact Us</span></div>
  <div class="abs foot-item" style="left:131px;top:53px">
    <svg width="10" height="14" viewBox="0 0 10 14" style="margin-top:3px"><path d="M5 0a5 5 0 015 5c0 4-5 9-5 9S0 9 0 5a5 5 0 015-5z" fill="#ccc"/><circle cx="5" cy="5" r="2" fill="#262626"/></svg>
    <div>4410 Alder Grove Road<br>Poway, CA 92064</div>
  </div>
  <div class="abs foot-item" style="left:364px;top:53px;font-weight:700">
    <svg width="11" height="11" viewBox="0 0 24 24" style="margin-top:4px"><path fill="#ccc" d="M6.6 10.8a15 15 0 006.6 6.6l2.2-2.2a1 1 0 011-.25 11.4 11.4 0 003.6.57 1 1 0 011 1V20a1 1 0 01-1 1A17 17 0 013 4a1 1 0 011-1h3.5a1 1 0 011 1c0 1.25.2 2.45.57 3.57a1 1 0 01-.25 1z"/></svg>
    <div>(858) 555-0147</div>
  </div>
  <div class="abs foot-item" style="left:364px;top:77px">
    <svg width="11" height="8" viewBox="0 0 18 12" style="margin-top:6px"><rect width="18" height="12" fill="#ccc"/><path d="M0 0l9 7 9-7" fill="none" stroke="#262626" stroke-width="1.6"/></svg>
    <div>info@maplehollowcare.com</div>
  </div>
  <div class="abs social" aria-label="Social media links"><i></i><i></i><i></i><i></i></div>
  <div class="abs subscribe">
    <div class="input"><svg width="16" height="10" viewBox="0 0 18 12"><rect width="18" height="12" fill="#ccc"/><path d="M0 0l9 7 9-7" fill="none" stroke="#f4f4f4" stroke-width="1.6"/></svg>your e-mail address</div>
    <div class="btn">SUBSCRIBE</div>
  </div>
  <div class="abs copyright">Copyright © 2016 Maple Hollow Post Acute.<br>All Right Reserved</div>
</footer>

</body>
</html>
```